Simple, Professional and neat business card design for Vendralo Inc.

We're looking to re-vamp our business card design. We're a supplier of innovative feed ingredients for the North American animal agriculture industry. We are located in Lucknow, Ontario, Canada and our flagship product is a product that prevents milk fever in dairy cows when the calve, it is fed before calving and is very effective compared to other alternatives available on the market today.

Our company has Danish roots and we import all of our product from our Danish partner/manufacturer in Denmark. We like our design to embrace high professionalism while remaining neat and simple.

Target Market(s)

B2B, Feed Mills, Veterinary Clinics, Large integrators/producers,

Industry/Entity Type

Agribusiness

Contact Information for Business Card

We like the rounded corners because they make the card easy to sit in a wallet and not many use it so it makes the card stand out, just possibly something to take account for during the design.

As you can also see on the sliders below, looking for a that simple but proffesional scandinavian design.

Requirements
Nice to have
• Rounded corners
Should not have
• Too vibrant

```html
<!DOCTYPE html>
<html lang="en">
<head>
<meta charset="utf-8">
<title>Vendralo Inc. — Business Card</title>
<link href="https://fonts.googleapis.com/css2?family=Lato:wght@900&family=Overlock:wght@700&family=Roboto:wght@400&display=swap" rel="stylesheet">
<style>
  :root {
    --page-bg: #e6e1d9;
    --card-bg: #f3f2ee;
    --navy: #1f3f86;
    --navy-deep: #1a3574;
    --gold: #c9b27a;
    --gold-light: #dccb9c;
    --ink: #3a3a3a;
    --white: #ffffff;
  }
  * { margin: 0; padding: 0; box-sizing: border-box; }
  html, body {
    width: 1200px; height: 1054px; overflow: hidden;
    background: var(--page-bg);
  }
  .card {
    position: absolute; left: 100px; top: 225px;
    width: 1000px; height: 603px;
    background: var(--card-bg);
    border-radius: 18px;
    overflow: hidden;
    box-shadow: 0 6px 24px rgba(0,0,0,0.12);
    font-family: "Roboto", Arial, sans-serif;
    color: var(--ink);
  }
  .brand {
    position: absolute; left: 47px; top: 96px;
    display: flex; align-items: center; gap: 40px;
  }
  .brand-mark {
    width: 110px; height: 110px;
    background: var(--gold);
    border-radius: 14px;
  }
  .brand-name {
    font-family: "Lato", Arial, sans-serif;
    font-weight: 900; font-size: 86px; line-height: 1;
    color: var(--navy);
    letter-spacing: 0.5px;
  }
  .person { position: absolute; left: 47px; top: 340px; }
  .person-name {
    font-family: "Overlock", Georgia, serif;
    font-weight: 700; font-size: 39px; color: var(--navy);
    line-height: 1.1;
  }
  .person-role { font-size: 22px; margin-top: 6px; }
  .address {
    position: absolute; left: 47px; top: 470px;
    font-size: 23px; line-height: 35px;
  }
  .contacts {
    position: absolute; left: 540px; top: 338px;
    display: grid; grid-template-columns: 210px 200px;
    row-gap: 7px; font-size: 23px; line-height: 29px;
  }
  .contact { display: flex; align-items: center; gap: 14px; white-space: nowrap; }
  .contact.wide { grid-column: 1 / span 2; }
  .contact svg { width: 22px; height: 22px; fill: var(--navy); flex: none; }
  .footer-gold {
    position: absolute; left: 0; bottom: 0; width: 470px; height: 23px;
    background: linear-gradient(90deg, var(--gold-light), var(--gold));
  }
  .footer-band {
    position: absolute; right: 0; bottom: 0; width: 585px; height: 73px;
    background: linear-gradient(90deg, var(--navy), var(--navy-deep));
    clip-path: polygon(38px 0, 100% 0, 100% 100%, 0 100%);
    display: flex; align-items: center; padding-left: 115px;
  }
  .follow-label { color: var(--white); font-size: 23px; margin-right: 26px; }
  .social { display: flex; gap: 9px; }
  .social span {
    width: 32px; height: 32px; border-radius: 50%;
    background: var(--gold-light);
  }
</style>
</head>
<body>
  <div class="card">
    <div class="brand">
      <div class="brand-mark"></div>
      <div class="brand-name">VENDRALO INC.</div>
    </div>

    <div class="person">
      <div class="person-name">Mads Kristensen</div>
      <div class="person-role">Managing Director</div>
    </div>

    <div class="address">
      212 Harbour Street,<br>
      Elmridge, MB, Canada
    </div>

    <div class="contacts">
      <div class="contact">
        <svg viewBox="0 0 24 24"><path d="M7 2h10a2 2 0 0 1 2 2v16a2 2 0 0 1-2 2H7a2 2 0 0 1-2-2V4a2 2 0 0 1 2-2zm0 3v13h10V5H7zm5 14.2a1 1 0 1 0 0 2 1 1 0 0 0 0-2z"/></svg>
        519-555-0142
      </div>
      <div class="contact">
        <svg viewBox="0 0 24 24"><path d="M2 9c0-3 4-5 10-5s10 2 10 5v2h-5V8.5c-1.5-.6-3.2-.9-5-.9s-3.5.3-5 .9V11H2V9zm4 4h12l2 7H4l2-7zm6 1.5a2.5 2.5 0 1 0 0 5 2.5 2.5 0 0 0 0-5z"/></svg>
        519-555-0187
      </div>
      <div class="contact">
        <svg viewBox="0 0 24 24"><path d="M6.6 10.8a15.1 15.1 0 0 0 6.6 6.6l2.2-2.2a1 1 0 0 1 1-.25 11.4 11.4 0 0 0 3.6.57 1 1 0 0 1 1 1V20a1 1 0 0 1-1 1A17 17 0 0 1 3 4a1 1 0 0 1 1-1h3.5a1 1 0 0 1 1 1c0 1.250.2 2.45.57 3.6a1 1 0 0 1-.25 1L6.6 10.8z"/></svg>
        888-555-0123
      </div>
      <div class="contact">
        <svg viewBox="0 0 24 24"><path d="M7 3h10v5H7V3zM4 9h16a2 2 0 0 1 2 2v6h-4v4H6v-4H2v-6a2 2 0 0 1 2-2zm4 6v4h8v-4H8z"/></svg>
        519-555-0199
      </div>
      <div class="contact wide">
        <svg viewBox="0 0 24 24"><path d="M2 5h20v14H2V5zm2 2v.6l8 5 8-5V7H4zm0 3v7h16v-7l-8 5-8-5z"/></svg>
        mads@vendralo.com
      </div>
      <div class="contact wide">
        <svg viewBox="0 0 24 24"><path d="M12 2a10 10 0 1 0 0 20 10 10 0 0 0 0-20zm6.9 6h-3a15 15 0 0 0-1.3-3.9A8 8 0 0 1 18.9 8zM12 4c.8 1.1 1.5 2.5 1.9 4h-3.8c.4-1.5 1.1-2.9 1.9-4zM4.3 14a8 8 0 0 1 0-4h3.4a16 16 0 0 0 0 4H4.3zm.8 2h3a15 15 0 0 0 1.3 3.9A8 8 0 0 1 5.1 16zm3-8h-3a8 8 0 0 1 4.3-3.9A15 15 0 0 0 8.1 8zM12 20c-.8-1.1-1.5-2.5-1.9-4h3.8c-.4 1.5-1.1 2.9-1.9 4zm2.3-6H9.7a14 14 0 0 1 0-4h4.6a14 14 0 0 1 0 4zm.3 5.9a15 15 0 0 0 1.3-3.9h3a8 8 0 0 1-4.3 3.9zM16.3 14a16 16 0 0 0 0-4h3.4a8 8 0 0 1 0 4h-3.4z"/></svg>
        www.vendralo.com
      </div>
    </div>

    <div class="footer-gold"></div>
    <div class="footer-band">
      <span class="follow-label">Follow us on:</span>
      <div class="social">
        <span></span><span></span><span></span><span></span>
      </div>
    </div>
  </div>
</body>
</html>
```